Four in One (Flexible infographic for Content Management Industry)

See attachment.
A graphic depicting 4 products, where each can stand on its own and each can be combined with others, but where, if all are taken together, the best result is achieved (the "super product").
Intended use is web. See attached file as an example.
The most basic idea is as the attached diagram shows, where 4 rectangles are arranged in a quadrangle, with a middle rectangle in the center representing the combined 4 products. This concept is fine except it is a bit too obvious as it stands. We are looking for either a variation of this or another concept.
The audience is technical + professional + enterprise - NOT consumers. Hence the design should be conservative in nature.
We are aware of tools like as Canva or Pictogram where such graphics are available, but we are looking for something with a bit more imagination and flexibility.
This graphic should be targeted to web sites and be delivered with vector-based (SVG) graphics.

```html
<!DOCTYPE html>
<html lang="en">
<head>
<meta charset="utf-8">
<title>Four in One – Super Product</title>
<link rel="stylesheet" href="https://fonts.googleapis.com/css2?family=Montserrat:wght@400;600;700&display=swap">
<style>
  :root {
    --yellow: #e3b022;
    --blue: #1c7898;
    --green: #9bbe3c;
    --teal: #139782;
    --purple: #9d4493;
    --ink: #1a1a1a;
    --white: #ffffff;
    --bg: #ffffff;
  }
  * { box-sizing: border-box; margin: 0; padding: 0; }
  html, body {
    width: 1200px; height: 675px; overflow: hidden; background: var(--bg);
    font-family: "Montserrat", Arial, sans-serif; color: var(--ink);
  }
  .canvas { position: relative; width: 1200px; height: 675px; }
  .diagram { position: absolute; left: 0; top: 0; width: 1200px; height: 675px; }
  .segment-label {
    font-family: "Montserrat", Arial, sans-serif;
    font-weight: 600; font-size: 13px; fill: var(--white);
  }
  .core-label {
    font-family: "Montserrat", Arial, sans-serif;
    font-weight: 700; font-size: 19px; fill: var(--white);
  }
  .feature {
    position: absolute; white-space: nowrap;
    font-size: 14.6px; line-height: 17.5px; font-weight: 400;
  }
  .feature--left { left: 27.5px; }
  .feature--right { left: 825px; }
  .feature--top { top: 80px; }
  .feature--bottom { top: 441px; }
  .feature__intro { margin-bottom: 5px; }
  .feature__list { list-style: none; }
  .feature__list li { height: 25px; line-height: 25px; }
  .feature__list li::before { content: "\2022"; font-size: 9px; margin-right: 5px; vertical-align: 2px; }
  .feature__link {
    display: inline-block; margin-top: 2px;
    font-size: 18px; font-weight: 600; color: var(--ink); text-decoration: none;
  }
  .feature__link::after { content: "\25B8"; font-size: 12px; margin-left: 7px; vertical-align: 2px; }
</style>
</head>
<body>
<main class="canvas">
  <svg class="diagram" viewBox="0 0 1200 675" xmlns="http://www.w3.org/2000/svg" aria-label="Four products combining into the Super Product">
    <defs>
      <path id="arc-tl" d="M 406 337.5 A 194 194 0 0 1 600 143.5"/>
      <path id="arc-tr" d="M 600 143.5 A 194 194 0 0 1 794 337.5"/>
      <path id="arc-br" d="M 794 337.5 A 194 194 0 0 1 600 531.5"/>
      <path id="arc-bl" d="M 600 531.5 A 194 194 0 0 1 406 337.5"/>
    </defs>

    <path class="segment segment--documents" fill="var(--yellow)" d="M 362.9 323.75 A 237.5 237.5 0 0 1 586.25 100.4 L 586.25 174.1 A 164 164 0 0 0 436.6 323.75 Z"/>
    <path class="segment segment--security" fill="var(--blue)" d="M 613.75 100.4 A 237.5 237.5 0 0 1 837.1 323.75 L 763.4 323.75 A 164 164 0 0 0 613.75 174.1 Z"/>
    <path class="segment segment--digital" fill="var(--teal)" d="M 837.1 351.25 A 237.5 237.5 0 0 1 613.75 574.6 L 613.75 500.9 A 164 164 0 0 0 763.4 351.25 Z"/>
    <path class="segment segment--erp" fill="var(--green)" d="M 586.25 574.6 A 237.5 237.5 0 0 1 362.9 351.25 L 436.6 351.25 A 164 164 0 0 0 586.25 500.9 Z"/>

    <text class="segment-label"><textPath href="#arc-tl" startOffset="41%" text-anchor="middle">Document Management</textPath></text>
    <text class="segment-label"><textPath href="#arc-tr" startOffset="58%" text-anchor="middle">Security and Compliance</textPath></text>
    <text class="segment-label"><textPath href="#arc-br" startOffset="41%" text-anchor="middle">Digitital Transformation</textPath></text>
    <text class="segment-label"><textPath href="#arc-bl" startOffset="58%" text-anchor="middle">Enterprise Resource planning</textPath></text>

    <g class="icon icon--document">
      <path d="M545 125 h20 l9 9 v30 a2 2 0 0 1 -2 2 h-27 a2 2 0 0 1 -2 -2 v-37 a2 2 0 0 1 2 -2 z" fill="var(--white)"/>
      <path d="M565 125 v9 h9" fill="none" stroke="var(--yellow)" stroke-width="1.5"/>
      <g stroke="var(--yellow)" stroke-width="1.8" stroke-linecap="round">
        <line x1="549" y1="141" x2="567" y2="141"/>
        <line x1="549" y1="147" x2="567" y2="147"/>
        <line x1="549" y1="153" x2="561" y2="153"/>
      </g>
    </g>

    <g class="icon icon--cloud">
      <path d="M633 158 a8 8 0 0 1 0 -16 a12 12 0 0 1 23 -4 a9 9 0 0 1 6 20 z" fill="var(--white)"/>
      <path d="M639 148 l5 5 l9 -9" fill="none" stroke="var(--blue)" stroke-width="2.6" stroke-linecap="round" stroke-linejoin="round"/>
    </g>

    <g class="icon icon--modules" fill="var(--white)">
      <rect x="534" y="512" width="17" height="17" rx="3"/>
      <rect x="555" y="512" width="17" height="17" rx="3" transform="rotate(45 563.5 520.5)"/>
      <rect x="534" y="533" width="17" height="17" rx="3"/>
      <rect x="555" y="533" width="17" height="17" rx="3"/>
    </g>

    <g class="icon icon--archive">
      <rect x="626" y="510" width="39" height="40" rx="5" fill="var(--white)"/>
      <circle cx="645.5" cy="530" r="12" fill="var(--teal)"/>
      <g stroke="var(--white)" stroke-width="2.4" stroke-linecap="round">
        <line x1="639" y1="525" x2="652" y2="525"/>
        <line x1="637.5" y1="530" x2="653.5" y2="530"/>
        <line x1="641" y1="535" x2="650" y2="535"/>
      </g>
    </g>

    <circle class="core" cx="600" cy="337.5" r="146" fill="var(--purple)"/>
    <text class="core-label" x="600" y="343.5" text-anchor="middle">Super Product</text>
  </svg>

  <section class="feature feature--left feature--top">
    <p class="feature__intro">Streamline document organization, access, and<br>collaboration with easier file storage and<br>sharing, leading to more efficient workflows.</p>
    <ul class="feature__list">
      <li>Centralized Document Control</li>
      <li>Collaborative Workspace Integration</li>
      <li>Automated Compliance Tracking</li>
    </ul>
    <a class="feature__link" href="#">Learn More</a>
  </section>

  <section class="feature feature--right feature--top">
    <p class="feature__intro">Benefit from tailored cloud solutions, secure<br>data storage, and expert disaster recovery<br>planning for reliable and scalable IT operations.</p>
    <ul class="feature__list">
      <li>Custom Cloud Solutions</li>
      <li>Secure Data Storage</li>
      <li>Expert Disaster Recovery</li>
    </ul>
    <a class="feature__link" href="#">Learn More</a>
  </section>

  <section class="feature feature--left feature--bottom">
    <p class="feature__intro">Simplify management across finance, sales, and<br>operations, enabling better decision-making<br>and improved productivity.</p>
    <ul class="feature__list">
      <li>Integrated Business Processes</li>
      <li>Enhanced Decision-Making</li>
      <li>Productivity Improvement</li>
    </ul>
    <a class="feature__link" href="#">Learn More</a>
  </section>

  <section class="feature feature--right feature--bottom">
    <p class="feature__intro">Turn scanned documents into easily searchable<br>digital archives, boosting efficiency and<br>accessibility.</p>
    <ul class="feature__list">
      <li>Instant searchable Archives with OCR</li>
      <li>Automated Document Classification</li>
      <li>Corvanta Share and Cloud Blob Ready</li>
    </ul>
    <a class="feature__link" href="#">Learn More</a>
  </section>
</main>
</body>
</html>
```